80s style fun billboard for auto repair shop

A new design for our automotive shops’s advertisement billboard with an 80s-90s theme! Neon colors like photo example. Something eye catching but easy to read. Logos attached should be altered to match theme of advertisement. 1980s or 90s colors and theme. Details need to include an arrow and “1.2 miles ahead”, phone number “614-382-7091”, address “3859 W Pellham Ave”, and “best auto repair shop in town!” . Dimensions are 12'3"x 24'6"

Target Market(s)

Drive by attention

Industry/Entity Type

Automotive

Colors

Designer to choose colors to be used in the design.

Requirements
Must have
• My logo, address, phone number, tag line and badass 90s theme look!
Nice to have
• 80s color scheme, neon colors, use example photo for color ideas

```html
<!DOCTYPE html>
<html lang="en">
<head>
<meta charset="UTF-8">
<title>Halverton's Premier Auto &amp; Diesel Repair Shop</title>
<link rel="stylesheet" href="https://fonts.googleapis.com/css2?family=Bebas+Neue&family=Allura&display=swap">
<style>
  :root {
    --bg-deep: #0a1322;
    --bg-mid: #17304f;
    --neon-blue: #4cc8ff;
    --neon-blue-glow: #1a8fff;
    --neon-red: #ff3346;
    --neon-red-glow: #e0001a;
    --script-ink: #050505;
    --white: #ffffff;
    --badge-blue: #2a8ee0;
    --mascot-dark: #1a1a1a;
    --mascot-red: #c8232c;
  }
  html, body {
    margin: 0;
    padding: 0;
    overflow: hidden;
    background: var(--bg-deep);
  }
  .billboard {
    position: relative;
    width: 1200px;
    height: 600px;
    overflow: hidden;
    background:
      radial-gradient(ellipse at 45% 50%, var(--bg-mid) 0%, #0f2038 45%, var(--bg-deep) 100%);
    font-family: "Bebas Neue", "Arial Narrow", sans-serif;
  }
  .neon-frame {
    position: absolute;
    inset: 0;
  }
  .headline {
    position: absolute;
    left: 0;
    width: 800px;
    margin: 0;
    text-align: center;
    line-height: 1;
    font-weight: 400;
    white-space: nowrap;
    color: transparent;
  }
  .headline--blue {
    -webkit-text-stroke: 2px var(--neon-blue);
    filter: drop-shadow(0 0 4px var(--neon-blue-glow)) drop-shadow(0 0 8px var(--neon-blue-glow));
  }
  .town-name {
    top: 76px;
    font-size: 140px;
    letter-spacing: 2px;
  }
  .service-line {
    top: 355px;
    font-size: 140px;
    letter-spacing: 3px;
  }
  .premier-script {
    position: absolute;
    top: 200px;
    left: 0;
    width: 800px;
    text-align: center;
    font-family: "Allura", cursive;
    font-size: 145px;
    line-height: 1;
    color: var(--script-ink);
    text-shadow: 0 0 3px var(--white), 0 0 8px rgba(255,255,255,0.8);
  }
  .repair-line {
    top: 488px;
    font-size: 96px;
    letter-spacing: 3px;
    -webkit-text-stroke: 2px var(--neon-red);
    filter: drop-shadow(0 0 4px var(--neon-red-glow)) drop-shadow(0 0 8px var(--neon-red-glow));
  }
  .partner-name {
    position: absolute;
    left: 812px;
    top: 40px;
    width: 258px;
    text-align: center;
    font-size: 44px;
    line-height: 1;
    color: var(--white);
  }
  .tagline {
    position: absolute;
    left: 808px;
    top: 150px;
    width: 196px;
    margin: 0;
    text-align: center;
    font-size: 28px;
    line-height: 1.05;
    color: var(--neon-red);
    text-shadow: 0 0 6px var(--neon-red-glow);
  }
  .cert-badge {
    position: absolute;
    left: 815px;
    top: 229px;
    width: 162px;
    height: 162px;
    border-radius: 50%;
    background: var(--badge-blue);
  }
  .distance {
    position: absolute;
    left: 806px;
    top: 404px;
    width: 200px;
    display: flex;
    align-items: center;
    justify-content: center;
    gap: 6px;
    font-size: 30px;
    line-height: 1;
    color: var(--neon-blue);
    text-shadow: 0 0 6px var(--neon-blue-glow);
    white-space: nowrap;
  }
  .distance svg {
    width: 30px;
    height: 22px;
  }
  .mascot-art {
    position: absolute;
    left: 1015px;
    top: 162px;
    width: 172px;
    height: 286px;
    border-radius: 40px;
    background: linear-gradient(170deg, var(--mascot-dark) 0%, #3a3a3a 45%, var(--mascot-red) 75%, #e8e8e8 100%);
  }
  .phone-ribbon {
    position: absolute;
    left: 800px;
    top: 456px;
    width: 384px;
    height: 82px;
  }
  .phone-number {
    position: absolute;
    left: 800px;
    top: 462px;
    width: 384px;
    text-align: center;
    font-size: 74px;
    line-height: 1;
    color: var(--white);
    letter-spacing: 1px;
  }
  .address {
    position: absolute;
    left: 826px;
    top: 546px;
    display: flex;
    align-items: center;
    gap: 4px;
    font-size: 46px;
    line-height: 1;
    color: var(--white);
    white-space: nowrap;
  }
  .address svg {
    width: 26px;
    height: 36px;
  }
</style>
</head>
<body>
<main class="billboard">
  <svg class="neon-frame" viewBox="0 0 1200 600" width="1200" height="600" aria-hidden="true">
    <defs>
      <filter id="red-glow" x="-10%" y="-10%" width="120%" height="120%">
        <feGaussianBlur stdDeviation="5" result="blur"/>
        <feMerge><feMergeNode in="blur"/><feMergeNode in="blur"/><feMergeNode in="SourceGraphic"/></feMerge>
      </filter>
    </defs>
    <polyline points="162,523 26,505 26,83 400,30 775,83 775,505 637,523"
      fill="none" stroke="#ff2a40" stroke-width="8" stroke-opacity="0.5" filter="url(#red-glow)"/>
    <polyline points="162,523 26,505 26,83 400,30 775,83 775,505 637,523"
      fill="none" stroke="#ffffff" stroke-width="1.5"/>
  </svg>

  <h1 class="headline headline--blue town-name">HALVERTON’S</h1>
  <div class="premier-script">Premier</div>
  <p class="headline headline--blue service-line">AUTO &amp; DIESEL</p>
  <p class="headline repair-line">REPAIR SHOP!</p>

  <div class="partner-name">RJ’s Auto &amp; Express Lube</div>
  <p class="tagline">Best auto repair shop in town!</p>
  <div class="cert-badge" role="img" aria-label="Certification badge"></div>
  <div class="distance">
    <svg viewBox="0 0 30 22" aria-hidden="true">
      <path d="M2 11h22M16 3l9 8-9 8" fill="none" stroke="#4cc8ff" stroke-width="3.5" stroke-linecap="round" stroke-linejoin="round"/>
    </svg>
    <span>1.2 miles ahead</span>
  </div>
  <div class="mascot-art" role="img" aria-label="Illustrated mechanic mascot holding a wrench and oil can"></div>

  <svg class="phone-ribbon" viewBox="0 0 384 82" aria-hidden="true">
    <polygon points="4,4 380,4 366,41 380,78 4,78 18,41"
      fill="none" stroke="#ff2a40" stroke-width="7" stroke-opacity="0.5" filter="url(#red-glow)"/>
    <polygon points="4,4 380,4 366,41 380,78 4,78 18,41"
      fill="none" stroke="#ffd6da" stroke-width="2"/>
  </svg>
  <div class="phone-number">614-382-7091</div>

  <div class="address">
    <svg viewBox="0 0 24 34" aria-hidden="true">
      <path d="M12 1C5.9 1 1 5.9 1 12c0 8 11 21 11 21s11-13 11-21C23 5.9 18.1 1 12 1z" fill="#ffffff"/>
      <circle cx="12" cy="12" r="4.5" fill="#0f2038"/>
    </svg>
    <span>3859 W Pellham Ave</span>
  </div>
</main>
</body>
</html>
```